Needing a business Card for new fire company.

Velm, sales fire equipment and parts. We also do tree clearing for the forest service. My logo will be attached to this. I am also looking for a design that when people see the card it stick with them and they will remember my sales team giving it to them.

```html
<!DOCTYPE html>
<html lang="en">
<head>
<meta charset="utf-8">
<title>Velm Business Card</title>
<link href="https://fonts.googleapis.com/css2?family=Arimo:wght@400;700&display=swap" rel="stylesheet">
<style>
  :root {
    --bg: #2b2b2b;
    --card-white: #ffffff;
    --card-black: #1e1e1e;
    --fire-red: #c4262e;
    --ink: #1f1f1f;
    --ink-soft: #2a2a2a;
  }
  * { box-sizing: border-box; margin: 0; padding: 0; }
  html, body {
    width: 1200px; height: 988px; overflow: hidden;
    background: var(--bg);
    font-family: "Arimo", Arial, sans-serif;
  }
  .sheet {
    width: 1200px; height: 988px;
    display: flex; flex-direction: column; align-items: center; justify-content: center;
    gap: 40px;
  }
  .card {
    position: relative;
    width: 760px; height: 434px;
    border-radius: 22px;
    overflow: hidden;
  }
  .card--back { background: var(--card-black); display: flex; align-items: center; justify-content: center; }
  .card--front { background: var(--card-white); }

  .brand {
    display: flex; align-items: center; gap: 18px;
    font-weight: 700; letter-spacing: 6px; line-height: 1;
  }
  .brand__dot { width: 30px; height: 30px; border-radius: 50%; background: var(--fire-red); }
  .card--back .brand { font-size: 104px; color: var(--card-white); }
  .card--front .brand {
    position: absolute; left: 70px; top: 150px;
    font-size: 78px; color: var(--ink);
  }
  .card--front .brand__dot { width: 24px; height: 24px; }

  .divider {
    position: absolute; left: 385px; top: 70px;
    width: 1.5px; height: 195px; background: var(--fire-red);
  }
  .details { position: absolute; left: 412px; top: 60px; color: var(--ink-soft); z-index: 1; }
  .details__name { color: var(--fire-red); font-weight: 700; font-size: 32px; letter-spacing: 0.5px; }
  .details__title { font-size: 19px; margin-top: 4px; color: var(--ink); }
  .details__address { font-size: 16px; line-height: 1.35; margin-top: 12px; padding-left: 26px; }
  .contact { list-style: none; margin-top: 8px; font-size: 16px; line-height: 1.4; }
  .contact li { display: flex; align-items: center; gap: 8px; }
  .contact svg { width: 14px; height: 14px; flex: none; fill: var(--fire-red); }

  .swoosh { position: absolute; left: 0; top: 0; width: 760px; height: 434px; }
</style>
</head>
<body>
<main class="sheet">
  <section class="card card--back" aria-label="Card back">
    <div class="brand"><span class="brand__dot"></span>VELM</div>
  </section>

  <section class="card card--front" aria-label="Card front">
    <svg class="swoosh" viewBox="0 0 760 434" aria-hidden="true">
      <path d="M0,434 L0,398 C300,380 600,345 760,306 L760,434 Z" fill="var(--fire-red)"/>
      <path d="M300,374 C500,352 650,326 760,296" fill="none" stroke="var(--ink)" stroke-width="4"/>
    </svg>

    <div class="brand"><span class="brand__dot"></span>VELM</div>
    <div class="divider"></div>

    <div class="details">
      <h1 class="details__name">DANE HARLOW</h1>
      <p class="details__title">CEO/Founder</p>
      <p class="details__address">P.O. Box 48 Ridgefall AB<br>Country Name 4210</p>
      <ul class="contact">
        <li><svg viewBox="0 0 16 16"><path d="M3 1l3 3-2 2c1 2 3 4 5 5l2-2 3 3-2 3C6 15 1 10 1 3z"/></svg>02 5550 1427</li>
        <li><svg viewBox="0 0 16 16"><path d="M4 0h8v16H4zM5.5 2v10h5V2z"/></svg>0455 610 382</li>
        <li><svg viewBox="0 0 16 16"><path d="M0 3h16v10H0zM1.5 4.5L8 9l6.5-4.5"/></svg>info@velmfire.com</li>
        <li><svg viewBox="0 0 16 16"><circle cx="8" cy="8" r="7"/></svg>www.velmfire.com</li>
      </ul>
    </div>
  </section>
</main>
</body>
</html>
```